Need a simple buisness card for my plumbing business. Would like it to be black background with white text.

Industry/Entity Type

Business

Requirements
Must have
• On the front of the card I need to have,
TKW PLUMBING SERVICES
PLUMBERS, DRAINERS & GASFITTERS
Dorian Lessop
0491576038
Info@tkwplumbingservices.com.au
LIC No 518047k
ABN No 57091836254
On the back I need in point form
Domestic,industrial,commercial, all new installations, renovations, sewer renewals, repairs,
Fully licensed and insured
Nice to have
• A nice simple logo

```html
<!DOCTYPE html>
<html lang="en">
<head>
<meta charset="utf-8">
<title>TKW Plumbing Services – Business Card</title>
<link rel="stylesheet" href="https://fonts.googleapis.com/css2?family=Francois+One&display=swap">
<style>
  :root {
    --page-bg: #ececec;
    --card-bg: #0a0a0a;
    --pattern-a: #161616;
    --pattern-b: #0c0c0c;
    --ink: #ffffff;
    --mark: #e4ecf2;
    --divider: #9a9a9a;
    --shadow: rgba(0, 0, 0, 0.35);
  }
  * { box-sizing: border-box; margin: 0; padding: 0; }
  html, body {
    width: 1200px;
    height: 900px;
    overflow: hidden;
    background: var(--page-bg);
    font-family: "Francois One", "Arial Narrow", sans-serif;
    color: var(--ink);
  }
  .canvas { position: relative; width: 1200px; height: 900px; }
  .card {
    position: absolute;
    width: 640px;
    height: 380px;
    background: var(--card-bg);
    box-shadow: 0 6px 18px var(--shadow);
    overflow: hidden;
  }
  .card--services { left: 110px; top: 55px; }
  .card--contact { left: 450px; top: 470px; }
  .card__pattern {
    position: absolute;
    inset: 0;
    background: radial-gradient(ellipse at 50% 50%, var(--pattern-a) 0%, var(--pattern-b) 80%);
  }
  .brand-mark {
    position: absolute;
    border-radius: 50%;
    background: var(--mark);
  }
  .card--services .brand-mark { width: 88px; height: 88px; left: 276px; top: 48px; }
  .card--contact .brand-mark { width: 66px; height: 66px; left: 442px; top: 118px; }
  .brand-title {
    position: absolute;
    text-align: center;
    text-transform: uppercase;
    line-height: 1.05;
    letter-spacing: 0.5px;
  }
  .card--services .brand-title { left: 0; right: 0; top: 160px; font-size: 31px; }
  .card--contact .brand-title { left: 340px; width: 280px; top: 196px; font-size: 18px; }
  .service-list {
    position: absolute;
    list-style: none;
    font-size: 14px;
    line-height: 1.2;
    letter-spacing: 0.3px;
  }
  .service-list li::before {
    content: "";
    display: inline-block;
    width: 5px; height: 5px;
    border-radius: 50%;
    background: var(--ink);
    margin: 0 8px 2px 0;
    vertical-align: middle;
  }
  .service-list--left { left: 120px; top: 295px; }
  .service-list--right { left: 405px; top: 265px; }
  .contact-name {
    position: absolute;
    left: 70px; top: 100px;
    font-size: 24px;
    letter-spacing: 0.5px;
  }
  .contact-details {
    position: absolute;
    left: 70px; top: 172px;
    font-size: 14px;
    line-height: 1.5;
    list-style: none;
  }
  .card__divider {
    position: absolute;
    left: 330px; top: 40px;
    width: 2px; height: 300px;
    background: linear-gradient(to bottom, transparent, var(--divider) 45%, var(--ink) 55%, transparent);
  }
</style>
</head>
<body>
  <main class="canvas">
    <section class="card card--services" aria-label="Card back – services">
      <div class="card__pattern" role="img" aria-label="Faint repeating pattern of wrenches across the card"></div>
      <div class="brand-mark" aria-hidden="true"></div>
      <h1 class="brand-title">TKW Plumbing Services<br>Plumbers, Drainers &amp; Gasfitters</h1>
      <ul class="service-list service-list--left">
        <li>Domestic</li>
        <li>Industrial</li>
        <li>Commercial</li>
        <li>All new installations</li>
      </ul>
      <ul class="service-list service-list--right">
        <li>Renovations</li>
        <li>Sewer renewals</li>
        <li>Repairs</li>
        <li>Fully licensed and insured</li>
      </ul>
    </section>

    <section class="card card--contact" aria-label="Card front – contact">
      <div class="card__pattern" role="img" aria-label="Faint repeating pattern of wrenches across the card"></div>
      <h2 class="contact-name">Dorian Lessop</h2>
      <ul class="contact-details">
        <li>0491576038</li>
        <li>Info@tkwplumbingservices.com.au</li>
        <li>LIC No 518047k</li>
        <li>ABN No 57091836254</li>
      </ul>
      <div class="card__divider" aria-hidden="true"></div>
      <div class="brand-mark" aria-hidden="true"></div>
      <p class="brand-title">TKW Plumbing Services<br>Plumbers, Drainers &amp; Gasfitters</p>
    </section>
  </main>
</body>
</html>
```